Business Card design for a skin clinic

i would like a business card design for our skin clinic.
our logo colors are Blue and Grey and Bule /white.
we are searching for a minimalistic design yet very elegant,dynamic and professional which can reflect a professional medical skin care clinic( not a beauty salon).
THE DESGIN IS NOT FOR A PERSON IT WILL BE USED IN THE CLINIC FOR CLIENTS SO THERE SHOULD BE NO NAME OF A PERSON ONLY THE CLINIC NAME AND THE CONTACT INFO

Target Market(s)
young and old womens
Industry/Entity Type
Business
Contact Information for Business Card
we have 2 address and both should be on the card.
address A: Lindenhoflaan 214B, 3041KP Rotterdam, Tel 010 483 21 95
address B: Zonnewijzerstraat 238, 1062RT Amsterdam Tel 020 571 3829
website www.huidpuntzorg.nu, email info@huidpuntzorg.nu
Look and feel
Each slider illustrates characteristics of the customer's brand and the style your logo design should communicate.

```html
<!DOCTYPE html>
<html lang="nl">
<head>
<meta charset="utf-8">
<title>Huidpuntzorg – visitekaartje</title>
<link href="https://fonts.googleapis.com/css2?family=Questrial&display=swap" rel="stylesheet">
<style>
  :root {
    --stage: #e6e9eb;
    --card-white: #ffffff;
    --card-dark: #3a3f47;
    --brand-blue: #2f7cc6;
    --text-grey: #4a4d52;
    --rule-grey: #b9bcc0;
    --text-light: #f2f3f5;
    --photo-a: #3a3f47;
    --photo-b: #6b6660;
  }
  * { box-sizing: border-box; margin: 0; padding: 0; }
  html, body {
    width: 1200px; height: 900px; overflow: hidden;
    background: var(--stage);
    font-family: "Questrial", "Century Gothic", sans-serif;
  }
  .stage { position: relative; width: 1200px; height: 900px; }
  .card {
    position: absolute; left: 250px; width: 700px; height: 400px;
    box-shadow: 0 6px 18px rgba(0,0,0,0.12);
    overflow: hidden;
  }
  .card--front { top: 40px; background: var(--card-white); color: var(--text-grey); }
  .card--back  { top: 460px; background: var(--card-dark); color: var(--text-light); }

  /* front */
  .brand-name {
    font-size: 36px; letter-spacing: 3px; color: var(--brand-blue);
    text-transform: uppercase; line-height: 1; white-space: nowrap;
  }
  .card--front .brand-name { position: absolute; left: 60px; top: 72px; }
  .rule { position: absolute; height: 1px; background: var(--rule-grey); }
  .rule--top { left: 380px; right: 40px; top: 122px; }
  .rule--mid { left: 40px; width: 320px; top: 170px; }
  .contact { position: absolute; font-size: 17px; line-height: 1.45; letter-spacing: 0.5px; }
  .contact p + p { margin-top: 22px; }
  .contact--amsterdam { left: 60px; top: 200px; }
  .contact--rotterdam { left: 380px; top: 150px; }

  /* back */
  .photo {
    position: absolute; right: 0; top: 0; width: 360px; height: 100%;
    background: linear-gradient(90deg, var(--photo-a) 0%, var(--photo-b) 55%, var(--photo-a) 100%);
    opacity: 0.85;
  }
  .card--back .brand-name {
    position: absolute; left: 150px; top: 150px;
    color: var(--text-light); font-size: 40px;
  }
  .website {
    position: absolute; left: 330px; top: 298px; font-size: 17px; letter-spacing: 1px;
    color: var(--text-light);
  }
</style>
</head>
<body>
<main class="stage">
  <section class="card card--front" aria-label="Voorkant visitekaartje">
    <div class="brand-name">Huidpuntzorg</div>
    <div class="rule rule--top"></div>
    <div class="rule rule--mid"></div>
    <div class="contact contact--amsterdam">
      <p>Zonnewijzerstraat 238,<br>1062RT Amsterdam</p>
      <p>Tel: 020 571 3829</p>
    </div>
    <div class="contact contact--rotterdam">
      <p>Lindenhoflaan 214B,<br>3041KP Rotterdam</p>
      <p>Tel: 010 483 21 95</p>
      <p>info@huidpuntzorg.nu</p>
    </div>
  </section>

  <section class="card card--back" aria-label="Achterkant visitekaartje">
    <div class="photo" role="img" aria-label="Portretfoto van een vrouw met verzorgde huid, hand tegen de wang"></div>
    <div class="brand-name">Huidpuntzorg</div>
    <div class="website">www.huidpuntzorg.nu</div>
  </section>
</main>
</body>
</html>
```